Trifold - Harbor Lantern Therapy

Maren Holloway, Psy.D.Licensed Psychologist

this is for hypnosis and meditation
I like decorative font for my name (conservative decorative)

calming effect is most imortant

Target Market(s)

clients with depression, pain, anxiety - adults and aged

Industry/Entity Type

Conservative

Font styles to use
Serif

Colors
abd037
85cae6
cadf82
34a7d7
ffffff
886aae
6b449b

Requirements
Must have
• I like zen-like calming effects. lime Green, light blues and purple. I like waves and color.
• I like water and light, flowers and plants - bamboo, stacking rocks, ocean, water, lotus flowers
Should not have
• not too much purple
• Mostly green and blue

```html
<!DOCTYPE html>
<html lang="en">
<head>
<meta charset="utf-8">
<title>Harbor Lantern Therapy – Trifold</title>
<link href="https://fonts.googleapis.com/css2?family=Lato:wght@300;400;700;900&display=swap" rel="stylesheet">
<style>
:root{
  --purple:#6b449b;
  --purple-soft:#886aae;
  --lavender:#e9e1f2;
  --lime:#abd037;
  --lime-soft:#cadf82;
  --sky:#85cae6;
  --ocean:#34a7d7;
  --white:#ffffff;
  --ink:#222222;
  --backdrop-dark:#464646;
  --backdrop-light:#666666;
}
*{box-sizing:border-box;margin:0;padding:0}
html,body{width:1200px;height:781px;overflow:hidden}
body{
  position:relative;
  font-family:"Lato",sans-serif;
  color:var(--ink);
  background:linear-gradient(to bottom,var(--backdrop-dark) 0 606px,var(--backdrop-light) 606px 781px);
}
.sheet{position:absolute;top:62px;width:513px;height:657px;background:var(--white);overflow:hidden}
.sheet--outside{left:70px}
.sheet--inside{left:617px}
.sheet-art{position:absolute;inset:0}
.flip{position:absolute;transform:rotate(180deg)}
.abs{position:absolute;white-space:nowrap}

/* outside: cover block */
.cover-block{left:270px;top:18px;width:243px;height:184px}
.cover-name{left:22px;top:10px;font-size:18px;font-weight:900;color:var(--purple)}
.cover-line{left:22px;font-size:17px;font-weight:300;color:var(--lime);letter-spacing:.3px}
.cover-spec{left:22px;top:82px;font-size:11.5px;font-weight:700;color:var(--purple);line-height:16px}
.cover-phone{left:22px;top:116px;font-size:19px;font-weight:300;color:var(--lime);letter-spacing:.5px}
.cover-band{position:absolute;left:0;top:146px;width:243px;height:36px;background:var(--purple);border-radius:0 20px 20px 0;color:var(--white);font-size:8.5px;line-height:11px;padding:7px 22px}

/* outside: office + motto */
.office{left:29px;top:276px;line-height:17.5px}
.office-title{font-size:14px;font-weight:400;color:var(--ink);margin-bottom:4px}
.office-address{font-size:14.5px;font-weight:700;color:var(--purple);line-height:17.5px}
.office-web{font-size:14px;color:var(--ink);margin-top:5px}
.motto{left:295px;top:277px;color:var(--white);font-weight:700;font-size:15.5px;line-height:20px;text-shadow:0 1px 2px rgba(0,40,60,.45)}
.motto .gap{margin-top:14px}

/* outside: services block */
.services-block{left:0;top:441px;width:513px;height:216px}
.services-title{position:absolute;left:26px;top:30px;font-size:20px;font-weight:300;color:var(--ink);letter-spacing:.3px}
.services-col{position:absolute;top:57px;font-size:8.2px;line-height:11.1px;color:var(--ink)}
.services-col--a{left:26px;width:208px}
.services-col--b{left:256px;width:224px}
.services-col p{margin-bottom:4px}
.svc{color:var(--purple);font-weight:700}
.fee{position:absolute;left:0;right:0;top:200px;text-align:center;font-size:8.4px;font-weight:700;color:var(--ink)}

/* inside */
.section{position:absolute;left:0;width:513px}
.section--what{top:0;height:224px}
.section--clear{top:224px;height:217px}
.section--bio{top:441px;height:216px}
.h-what{position:absolute;left:26px;top:24px;font-size:17px;font-weight:400;color:var(--purple)}
.h-what strong{font-weight:700}
.what-body{position:absolute;left:26px;top:46px;width:465px;font-size:9.4px;line-height:11.6px;color:var(--ink)}
.what-lead{position:absolute;left:26px;top:133px;font-size:9.2px;font-weight:700;color:var(--ocean)}
.issue-list{position:absolute;top:152px;list-style:none;font-size:9.4px;line-height:11.8px}
.issue-list li::before{content:"• "}
.issue-list--a{left:26px}
.issue-list--b{left:263px}
.h-clear{position:absolute;left:26px;top:14px;font-size:15.5px;font-weight:400;color:var(--purple);letter-spacing:.2px}
.clear-body{position:absolute;left:26px;top:38px;width:224px;font-size:5.6px;line-height:7.55px;text-align:justify;color:var(--ink)}
.session-box{position:absolute;left:261px;top:46px;width:242px;height:155px;background:var(--purple);border-radius:6px;color:var(--white);padding:8px 10px}
.session-box h3{font-size:14.5px;font-weight:400;margin-bottom:4px}
.session-box h3 strong{font-weight:700}
.session-box .box-text{font-size:5.6px;line-height:7.4px}
.session-box ul{margin-top:8px;padding-left:12px;font-size:8px;line-height:9.8px}
.h-bio{position:absolute;left:26px;top:33px;font-size:16px;font-weight:400;color:var(--purple)}
.bio-body{position:absolute;left:26px;top:54px;width:329px;font-size:9.4px;line-height:11.7px;text-align:justify;color:var(--ink)}
.portrait{position:absolute;left:367px;top:29px;width:124px;height:161px;background:linear-gradient(160deg,#f4f4f2,#dfe7ea 60%,#8fd3d6)}
</style>
</head>
<body>

<!-- Outside of the trifold -->
<section class="sheet sheet--outside">
  <svg class="sheet-art" width="513" height="657" viewBox="0 0 513 657">
    <defs>
      <radialGradient id="lotusTone" cx="0.3" cy="0.45" r="0.8">
        <stop offset="0" stop-color="#f3c46a"/>
        <stop offset="0.18" stop-color="#e79ad8"/>
        <stop offset="0.55" stop-color="#b862c9"/>
        <stop offset="0.85" stop-color="#6d9a54"/>
        <stop offset="1" stop-color="#3f6e3b"/>
      </radialGradient>
      <linearGradient id="seaTone" x1="0" y1="0" x2="0" y2="1">
        <stop offset="0" stop-color="#2f8aa3"/>
        <stop offset="0.5" stop-color="#3fa9bf"/>
        <stop offset="1" stop-color="#1d6f88"/>
      </linearGradient>
      <linearGradient id="mistTop" x1="0" y1="0" x2="0" y2="1">
        <stop offset="0" stop-color="#cbb9e0"/>
        <stop offset="1" stop-color="#ffffff" stop-opacity="0"/>
      </linearGradient>
      <linearGradient id="mistBottom" x1="0" y1="1" x2="0" y2="0">
        <stop offset="0" stop-color="#b9a2d6"/>
        <stop offset="1" stop-color="#ffffff" stop-opacity="0"/>
      </linearGradient>
    </defs>
    <g role="img" aria-label="Photo of a pink lotus flower in soft light">
      <rect x="0" y="0" width="513" height="226" fill="url(#lotusTone)"/>
    </g>
    <path d="M312,0 C272,22 262,62 268,102 C274,150 236,192 212,224 L513,224 L513,0 Z" fill="var(--white)"/>
    <path d="M312,0 C272,22 262,62 268,102 C274,150 236,192 212,224" fill="none" stroke="var(--lime)" stroke-width="5"/>
    <g role="img" aria-label="Photo of calm turquoise ocean water">
      <rect x="150" y="224" width="363" height="217" fill="url(#seaTone)"/>
    </g>
    <path d="M0,224 L212,224 C256,256 292,296 284,340 C276,388 246,418 232,441 L0,441 Z" fill="var(--white)"/>
    <path d="M212,224 C256,256 292,296 284,340 C276,388 246,418 232,441" fill="none" stroke="var(--lime)" stroke-width="5"/>
    <path d="M0,441 L513,441 L513,657 L0,657 Z" fill="var(--white)"/>
    <path d="M0,441 L513,441 L513,476 C380,462 200,500 0,470 Z" fill="url(#mistTop)"/>
    <path d="M0,657 L513,657 L513,618 C360,640 180,600 0,630 Z" fill="url(#mistBottom)"/>
  </svg>

  <div class="flip cover-block">
    <p class="abs cover-name">Maren Holloway, Psy.D.</p>
    <p class="abs cover-line" style="top:35px">Live Well, Love Well</p>
    <p class="abs cover-line" style="top:57px">Licensed Psychologist</p>
    <p class="abs cover-spec">Specializing in Adults and Harbor<br>Lantern Therapy</p>
    <p class="abs cover-phone">555 014-2290</p>
    <div class="cover-band">Unleashing the Power of the Mind<br>for Healing and Well-being</div>
  </div>

  <address class="abs office" style="font-style:normal">
    <p class="office-title">Office Location:</p>
    <p class="office-address">Seagrass Commons<br>410 Shoreline Dr #12<br>Cove Harbor, FL 32990<br>555 014-2290</p>
    <p class="office-web">www.harborlanternwellness.com</p>
  </address>

  <div class="abs motto">
    <p>Maren Holloway, Psy.D.</p>
    <p>Licensed Psychologist</p>
    <p class="gap">Heal the Past</p>
    <p>Embrace the Present</p>
    <p>Create the Future</p>
  </div>

  <div class="flip services-block">
    <h2 class="services-title">Psychological Services</h2>
    <div class="services-col services-col--a">
      <p><span class="svc">Initial evaluation</span> – Mental health assessment, diagnosis and comprehensive wellness planning.</p>
      <p><span class="svc">Harbor Lantern Therapy (HLT)</span> – Resolve emotional distress, heartbreak and grief. HLT clears trauma at the subconscious level with guided communication. The most troubling of memories are worked through and clients gain a sense of clarity, peace and power. Only a couple of sessions are needed to experience dramatic and long-lasting effects.</p>
    </div>
    <div class="services-col services-col--b">
      <p><span class="svc">Eye Movement Desensitization and Reprocessing (EMDR)</span> – Evidence-based treatment for post-traumatic stress, anxiety, depression and adverse experiences. Experience relief and empowerment. More information at calmpath.org.</p>
      <p><span class="svc">Short-term talk therapy</span> – Psychotherapy to create a more satisfying life. Proactive approach to seeking effective solutions for your most pressing emotional and relational problems.</p>
      <p><span class="svc">Meditation for Wellness</span> – Personalized meditation for calm, healing and well-being.</p>
    </div>
    <p class="fee">Fee Information: Most major plans accepted and filed.</p>
  </div>
</section>

<!-- Inside of the trifold -->
<section class="sheet sheet--inside">
  <svg class="sheet-art" width="513" height="657" viewBox="0 0 513 657" aria-hidden="true">
    <defs>
      <linearGradient id="veilDown" x1="0" y1="0" x2="0" y2="1">
        <stop offset="0" stop-color="#d9cbe9"/>
        <stop offset="1" stop-color="#ffffff" stop-opacity="0"/>
      </linearGradient>
      <linearGradient id="veilUp" x1="0" y1="1" x2="0" y2="0">
        <stop offset="0" stop-color="#d9cbe9"/>
        <stop offset="1" stop-color="#ffffff" stop-opacity="0"/>
      </linearGradient>
    </defs>
    <path d="M0,0 L513,0 L513,30 C380,14 200,44 0,22 Z" fill="url(#veilDown)"/>
    <path d="M0,224 L513,224 L513,196 C360,212 170,182 0,204 Z" fill="url(#veilUp)"/>
    <path d="M0,224 L513,224 L513,254 C360,236 180,262 0,244 Z" fill="url(#veilDown)"/>
    <path d="M0,441 L513,441 L513,414 C350,432 170,400 0,420 Z" fill="url(#veilUp)"/>
    <path d="M0,441 L513,441 L513,476 C360,458 170,486 0,466 Z" fill="url(#veilDown)"/>
    <path d="M0,657 L513,657 L513,626 C360,644 170,612 0,634 Z" fill="url(#veilUp)"/>
    <line x1="0" y1="126" x2="513" y2="126" stroke="#e4e4ea" stroke-width="1"/>
  </svg>

  <div class="section section--what">
    <h2 class="h-what">What is <strong>Harbor Lantern Therapy (HLT)</strong></h2>
    <p class="what-body">HLT dramatically enhances mood, creates calm, eases grief, optimizes health and promotes success. It is a form of hypnosis that clears stuck patterns of thinking and feeling at the subconscious level. Past emotionally charged memories are cleared. You do not have to talk about problems, share scattered thoughts, cry nor re-experience uncomfortable emotions. You are guided to engage in deep brain processing to create an internal shift for automatic changes in thoughts, feelings and behaviors. Profound change happens within your nervous system facilitating lasting positive effects. Only one or two sessions are needed to experience immediate symptom relief.</p>
    <p class="what-lead">HLT is effective for many of life's problems including:</p>
    <ul class="issue-list issue-list--a">
      <li>PTSD, Sexual Abuse and Childhood Abuse</li>
      <li>Grief, Infidelity and Heartbreak</li>
      <li>Relationship issues</li>
      <li>Anger and Resentment</li>
    </ul>
    <ul class="issue-list issue-list--b">
      <li>Guilt / Shame</li>
      <li>Anxiety / Fear</li>
      <li>Nightmares / Insomnia</li>
      <li>Stress-related symptoms and Pain</li>
    </ul>
  </div>

  <div class="section section--clear">
    <h2 class="h-clear">CLEARING OLD STUFF AND MAKING WAY FOR NEW BEGINNINGS</h2>
    <p class="clear-body">HLT gently eases low mood and restores calm even when you have been unable to change how you feel, think or act. When something is painful or disturbing, it leaves a lasting impression. Even when the experience is over, deeper parts of the mind may continue to respond as if the distress is still present. Fed by that ongoing influence, emotional problems, unhelpful habits and relationship strain can feel impossible to overcome. You may clearly see the value of changing, yet your deeper mind stays on guard. In HLT the subconscious mind is engaged and the weight of past events is released. Energy that was held is freed and healing takes place. Old patterns and painful feelings are replaced by steadiness, well-being and motivation for the life you want. HLT is a form of guided focus that clears stuck patterns of thinking and feeling below awareness. Charged memories settle without retelling them. You will not need to relive hard emotions or explain every detail. Guided, focused processing creates an inner shift for lasting change in thoughts, feelings and behaviors. Only one or two sessions are often needed for relief.</p>
    <aside class="session-box">
      <h3>What happens <strong>in an HLT Session?</strong></h3>
      <p class="box-text">Stress is held in both the mind and the body. In HLT you will feel deep physical calm as you are guided toward emotional resolution in a gentle, creative and even light-hearted way. You reach inner resources of clarity, wisdom and peace. As Elias Brandt says: “we all carry a steady light within, we only forget it is there.” From this place of light, hard memories are softly reframed with new meaning. You leave the session feeling peaceful and grounded from within.</p>
      <ul>
        <li>Discover and resolve subconscious causes for emotional and behavioral difficulties</li>
        <li>Eliminate unconscious conflicts blocking desired change</li>
        <li>Promote mind / body healing</li>
      </ul>
    </aside>
  </div>

  <div class="section section--bio">
    <h2 class="h-bio">Dr. Maren Holloway</h2>
    <p class="bio-body">Dr. Holloway is a licensed clinical psychologist specializing in adults and seniors. She treats people for depression, anxiety, grief, sexual trauma, PTSD, relationship issues, infidelity, divorce and stress-related symptoms. She has over 20 years of clinical experience in mental health and is an adjunct counseling professor at Lakeview University. She received her Master's and Doctorate degrees in Clinical Psychology from Kestrel University in Coral Bay, Hawaii. She earned a Bachelor's of Science degree in Rehabilitation Medicine from Northgate University in Ashford, Canada. At Harbor Lantern Wellness Center, she provides initial evaluations, assessment, diagnosis and comprehensive treatment planning. She will collaborate with you to create solutions for healing, empowerment and wellness.</p>
    <div class="portrait" role="img" aria-label="Portrait photo of Dr. Maren Holloway"></div>
  </div>
</section>

</body>
</html>
```